Postcard Design January 2015

I need a postcard designed to introduce my company to potential new customers in the UK. My company is QT Page Solutions based in Chester and we represent one of Poland's leading and long established book printers. We offer competitive pricing, consistently high levels of print and binding quality and industry leading levels of customer service. We have been meeting the print requirements of UK publishers for more than 10 years.

```html
<!DOCTYPE html>
<html lang="en">
<head>
<meta charset="utf-8">
<title>QT Page Solutions – Postcard</title>
<link rel="stylesheet" href="https://fonts.googleapis.com/css2?family=Rokkitt:wght@400&family=Raleway:ital,wght@0,400;0,700;1,600&family=Cinzel:wght@700&display=swap">
<style>
  :root {
    --stage: #000000;
    --card: #ffffff;
    --ink: #2a2a2a;
    --ink-soft: #3b3b3b;
    --magenta: #e0157f;
    --orange: #f6a323;
    --brand-blue: #1a8fd6;
    --rule: #c2316f;
    --panel: rgba(255, 255, 255, 0.86);
  }
  * { box-sizing: border-box; margin: 0; padding: 0; }
  html, body { width: 1200px; height: 488px; overflow: hidden; background: var(--stage); }
  .stage { position: relative; width: 1200px; height: 488px; }

  .postcard {
    position: absolute; top: 30px; width: 561px; height: 434px;
    overflow: hidden; background: var(--card);
  }
  .postcard--front { left: 28px; }
  .postcard--back { left: 613px; }

  /* Front */
  .front__photo {
    position: absolute; inset: 0;
    background:
      linear-gradient(90deg,
        #3a3a3a 0%, #8c8c8c 6%, #d8d8d8 10%, #5a5a5a 14%, #e6cb2a 17%, #8a8a8a 22%, #bdbdbd 25%,
        #f0f0f0 30%, #f0f0f0 82%,
        #f4c21a 85%, #f08a2a 88%, #e2338f 92%, #9c3fb3 96%, #3b8be0 100%);
  }
  .front__panel {
    position: absolute; left: 113px; top: 0; width: 336px; height: 100%;
    background: var(--panel);
  }
  .front__headline {
    position: absolute; left: 113px; width: 336px; top: 20px;
    font-family: "Rokkitt", serif; font-weight: 400; font-size: 28px; line-height: 29px;
    text-align: center; color: var(--ink);
  }
  .ribbon {
    position: absolute; left: 103px; width: 355px; height: 26px;
    display: flex; align-items: center; justify-content: center;
    font-family: "Raleway", sans-serif; font-weight: 700; font-size: 13px;
  }
  .ribbon--quality { top: 114px; background: var(--magenta); color: #fff; }
  .ribbon--service { top: 148px; background: var(--orange); color: var(--ink); }
  .front__features {
    position: absolute; left: 158px; top: 182px; width: 285px;
    font-family: "Raleway", sans-serif; font-size: 11.3px; line-height: 15px; color: var(--ink-soft);
    list-style: none;
  }
  .front__features li { position: relative; margin-bottom: 2px; }
  .front__features li::before {
    content: "•"; position: absolute; left: -15px; top: 0; font-size: 9px;
  }
  .front__enquiry {
    position: absolute; left: 129px; top: 337px; width: 120px;
    font-family: "Raleway", sans-serif; font-style: italic; font-weight: 600; font-size: 9px; line-height: 11px; color: var(--ink);
  }
  .brand {
    position: absolute; text-align: center; color: var(--ink);
  }
  .brand__mark { display: block; margin: 0 auto 5px; width: 22px; height: 22px; background: var(--brand-blue); }
  .brand__name { display: block; font-family: "Cinzel", serif; font-weight: 700; white-space: nowrap; }
  .brand__contact { display: block; font-family: "Raleway", sans-serif; font-size: 11px; margin-top: 2px; }
  .front__brand { left: 150px; width: 290px; top: 333px; }
  .front__brand .brand__name { font-size: 21px; }

  /* Back */
  .back__photo {
    position: absolute; left: 0; top: 0; width: 298px; height: 340px;
    background:
      linear-gradient(180deg, rgba(255,255,255,0) 40%, #ffffff 98%),
      linear-gradient(155deg, #5a6f86 0%, #9fb0c2 22%, #d9dde2 38%, #e7a6a0 52%, #c9cfe0 64%, #eceef2 80%);
  }
  .back__copy {
    position: absolute; left: 0; width: 298px; top: 133px;
    text-align: center; font-family: "Raleway", sans-serif; font-weight: 700; font-size: 13.5px; line-height: 18px; color: var(--ink);
  }
  .back__line { display: block; }
  .back__rule { display: block; width: 170px; height: 1px; margin: 2px auto 4px; background: var(--rule); }
  .back__enquiry {
    position: absolute; left: 0; width: 298px; top: 239px; text-align: center;
    font-family: "Raleway", sans-serif; font-style: italic; font-weight: 600; font-size: 9.5px; color: var(--ink);
  }
  .back__brand { left: 0; width: 298px; top: 258px; }
  .back__brand .brand__name { font-size: 20px; }
</style>
</head>
<body>
<main class="stage">

  <section class="postcard postcard--front" aria-label="Postcard front">
    <div class="front__photo" role="img" aria-label="Photograph of printing press gears and rollers with coloured ink cylinders"></div>
    <div class="front__panel"></div>
    <h1 class="front__headline">Poland's Leading And<br>Long Established<br>Book Printers</h1>
    <p class="ribbon ribbon--quality">High Quality Book Printing and Binding</p>
    <p class="ribbon ribbon--service">Competitive pricing • Excellent customer service</p>
    <ul class="front__features">
      <li>We produce paperback and hardback books in mono or full colour. Binding options include sewn, perfect, Wiro-o and saddle stitched</li>
      <li>Print finishing includes lamination, spot UV and foil stamping</li>
      <li>We have state of the art production equipment, use top quality materials and follow strict quality control procedures</li>
      <li>We have weekly shipments in to the UK</li>
    </ul>
    <p class="front__enquiry">Further information, quotations or samples.</p>
    <div class="brand front__brand">
      <span class="brand__mark"></span>
      <span class="brand__name">QT PAGE SOLUTIONS</span>
      <span class="brand__contact">Address, Phone. email</span>
    </div>
  </section>

  <section class="postcard postcard--back" aria-label="Postcard back">
    <div class="back__photo" role="img" aria-label="Photograph of printed sheets running through a press roller"></div>
    <p class="back__copy">
      <span class="back__line">High Quality Book</span>
      <span class="back__line">Printing and Binding</span>
      <span class="back__rule"></span>
      <span class="back__line">Competitive pricing</span>
      <span class="back__rule"></span>
      <span class="back__line">Excellent customer service</span>
    </p>
    <p class="back__enquiry">Further information, quotations or samples.</p>
    <div class="brand back__brand">
      <span class="brand__mark"></span>
      <span class="brand__name">QT PAGE SOLUTIONS</span>
      <span class="brand__contact">Address, Phone. email</span>
    </div>
  </section>

</main>
</body>
</html>
```